Website for Life Strategies business

We need a website to present our video, audio and print content to subcribers at Kindred Ascent Partners. We will offer a team of coaches who can help people breakthrough the barriers that keep them from reaching their physical, spiritual, financial, leadership and relationship goals.

Target Market(s)

Anyone who needs help with strategies to take their life to a new level of success.

Industry/Entity Type

Life Coaching

Logo Text

Kindred Ascent Partners

Number of Pages Required

5+ page

Colors

Designer to choose colors to be used in the design.

Requirements
Must have
• The ability to present content as a package that includes Word Documents, videos and audio content as well as to be able to display books for sale. Each week their would be a new package for subscribers to access. It should provide the ability for subscribers to comment on the material and share how their lives were changed by the content. Should also include a shop page to offer merchandise for sale.
Nice to have
• Not sure
Should not have
• Not sure

```html
<!DOCTYPE html>
<html lang="en">
<head>
<meta charset="utf-8">
<title>Kindred Ascent Partners – Life Coaching</title>
<link href="https://fonts.googleapis.com/css2?family=Open+Sans:ital,wght@0,400;0,600;0,700;1,400&display=swap" rel="stylesheet">
<style>
:root{
  --green:#7dc142;
  --cyan:#1ba1d6;
  --ink:#1e1e1e;
  --text:#444;
  --muted:#777;
  --paper:#ffffff;
  --stone:#efefea;
  --mist:#e7e7e7;
  --night:#1b1b1b;
  --night-text:#cfcfcf;
}
*{box-sizing:border-box;margin:0;padding:0}
html,body{width:1200px;height:3830px;overflow:hidden}
body{font-family:"Open Sans",Arial,sans-serif;color:var(--text);background:var(--paper);position:relative}
a{color:inherit;text-decoration:none}

/* header */
.site-header{position:absolute;left:0;top:0;width:1200px;height:140px}
.brand{position:absolute;left:102px;top:36px;display:flex;align-items:center;gap:14px}
.brand-dot{width:58px;height:58px;border-radius:50%;background:var(--cyan)}
.brand-name{font-weight:700;font-size:20px;color:var(--cyan);line-height:1.15;width:160px}
.account{position:absolute;top:46px;height:44px;display:flex;align-items:center;gap:12px;padding:0 22px;color:#fff;font-size:15px;font-weight:600}
.account.login{left:835px;width:118px;background:var(--cyan)}
.account.register{left:965px;width:135px;background:var(--green)}
.account svg{width:16px;height:16px}

.main-nav{position:absolute;left:0;top:140px;width:1200px;height:38px;background:var(--cyan);display:flex;padding-left:102px}
.main-nav a{color:#fff;font-size:14px;font-weight:600;line-height:38px;padding:0 28px}
.main-nav a.active{background:var(--green);padding:0 36px}

/* hero */
.hero{position:absolute;left:0;top:178px;width:1200px;height:516px;
  background:linear-gradient(180deg,#1a2a66 0%,#3f5aa0 40%,#b98a78 72%,#3a2f3e 100%)}
.hero h1{position:absolute;left:102px;top:200px;color:#fff;font-size:33px;font-weight:600;line-height:1.25}
.btn{display:inline-block;background:var(--green);color:#fff;font-weight:600;font-size:15px;text-align:center}
.hero .btn{position:absolute;left:102px;top:302px;width:126px;height:43px;line-height:43px}

/* shared */
.section-title{font-size:31px;font-weight:600;color:var(--ink);text-align:center}
.section-title span,.card-title span{color:var(--green)}
.section-title span.cyan{color:var(--cyan)}
.divider{position:relative;height:18px;margin:14px auto 0}
.divider::before{content:"";position:absolute;left:0;right:0;top:8px;height:1px;background:#cfcfcf}
.divider i{position:absolute;left:50%;top:0;width:18px;height:18px;margin-left:-9px;border-radius:50%;background:#bdbdbd}
.lead{font-size:13px;line-height:1.75;color:var(--text);text-align:center}

/* about */
.about{position:absolute;left:0;top:694px;width:1200px;height:353px}
.about-photo{position:absolute;left:102px;top:46px;width:358px;height:273px;background:linear-gradient(135deg,#d9d4cc,#b7c4d6 60%,#4e8ec2);border:5px solid #e6e6e6}
.about h2{position:absolute;left:488px;top:28px;font-size:32px;font-weight:600;color:var(--ink)}
.about h2 span{color:var(--cyan)}
.about .divider{position:absolute;left:488px;top:88px;width:580px;margin:0}
.about .divider i{left:9px}
.about p{position:absolute;left:488px;top:126px;width:610px;font-size:13px;line-height:1.8}
.about .btn{position:absolute;left:488px;top:268px;width:112px;height:42px;line-height:42px}

/* help */
.help{position:absolute;left:0;top:1047px;width:1200px;height:472px;background:var(--stone)}
.help .section-title{margin-top:50px}
.help .divider{width:420px}
.help .lead{width:1080px;margin:20px auto 0}
.pillars{position:absolute;left:100px;top:200px;width:1000px;display:flex;justify-content:space-between}
.pillar{width:230px;text-align:center}
.pillar svg{width:128px;height:128px;display:block;margin:0 auto}
.pillar h3{font-size:18px;font-weight:600;color:var(--ink);margin-top:12px}
.pillar p{font-size:12.5px;line-height:1.5;margin-top:4px}
.pillar p b{color:var(--green);font-weight:400}
.chev{position:absolute;top:290px;width:24px;height:40px}

/* services */
.services{position:absolute;left:0;top:1519px;width:1200px;height:671px}
.services .section-title{margin-top:36px}
.services .divider{width:420px}
.services .lead{width:1080px;margin:20px auto 0}
.services-mark{position:absolute;left:118px;top:220px;width:270px;text-align:center}
.services-mark .dot{width:150px;height:150px;border-radius:50%;background:var(--cyan);margin:0 auto}
.services-mark .name{font-size:26px;font-weight:700;color:var(--cyan);margin-top:20px;line-height:1.2}
.services-rule{position:absolute;left:426px;top:230px;width:2px;height:320px;background:var(--green)}
.service{position:absolute;left:446px;width:660px}
.service h3{font-size:15px;font-weight:600;color:var(--ink)}
.service p{font-size:13px;line-height:1.6;margin-top:6px}
.service::before{content:"";position:absolute;left:-20px;top:6px;border:7px solid transparent;border-left-color:var(--green)}

/* packages */
.packages{position:absolute;left:0;top:2190px;width:1200px;height:447px}
.packages-photo{position:absolute;left:0;top:0;width:600px;height:447px;background:linear-gradient(135deg,#c6dd8a,#8cbf4a 60%,#6aa232)}
.packages-panel{position:absolute;left:0;top:0;width:600px;height:447px;text-align:center;color:#fff}
.packages-panel svg{display:block;margin:100px auto 0;width:90px;height:90px}
.packages-panel h2{font-size:32px;font-weight:600;margin-top:16px}
.packages-panel p{font-size:20px;margin-top:2px}
.packages-panel .btn{background:#4a4a4a;margin-top:20px;width:124px;height:42px;line-height:42px}
.video-photo{position:absolute;left:600px;top:0;width:600px;height:447px;background:linear-gradient(135deg,#3d4650,#7c8a96 55%,#b6bcc2)}

/* books */
.books{position:absolute;left:0;top:2637px;width:1200px;height:414px}
.books .section-title{margin-top:40px}
.books .divider{width:420px}
.book-cover{position:absolute;left:145px;top:163px;width:135px;height:225px;background:linear-gradient(90deg,#1580b4,#29a8dc);box-shadow:6px 6px 10px rgba(0,0,0,.18)}
.book-info{position:absolute;left:324px;top:168px;width:790px}
.book-info h3{font-size:17px;font-weight:600;color:var(--ink);white-space:nowrap}
.book-info p{font-size:13px;line-height:1.75;margin-top:18px}
.book-info .btn{margin-top:28px;width:118px;height:42px;line-height:42px}

/* blog & testimonials */
.community{position:absolute;left:0;top:3051px;width:1200px;height:390px;background:var(--mist)}
.card{position:absolute;top:46px;width:485px;height:281px;background:#fff;padding:28px 22px}
.card.blog{left:102px}
.card.voices{left:613px}
.card-title{font-size:30px;font-weight:600;color:var(--ink)}
.card .divider{margin:10px 0 0;width:440px}
.card .divider i{left:9px}
.post{display:flex;gap:12px;margin-top:22px}
.post-date{width:38px;height:44px;background:var(--green);color:#fff;font-size:11px;text-align:center;line-height:1.2;padding-top:5px;flex:none}
.post h4{font-size:14px;font-weight:600;color:var(--ink)}
.post p{font-size:12px;line-height:1.5;margin-top:2px}
.quote{display:flex;gap:22px;margin-top:22px}
.avatar{width:88px;height:88px;border-radius:50%;background:linear-gradient(135deg,#c9d6e3,#8aa6c0);border:3px solid #eee;flex:none}
.quote p{font-size:12.5px;font-style:italic;line-height:1.6;color:var(--muted)}

/* footer */
.site-footer{position:absolute;left:0;top:3441px;width:1200px;height:342px;background:var(--night);color:var(--night-text)}
.foot-col{position:absolute;top:46px}
.foot-col h4{font-size:19px;font-weight:600;color:#fff;margin-bottom:12px}
.links li{list-style:none;font-size:13px;line-height:25px}
.links li::before{content:"› ";}
.contact-row{display:flex;gap:10px;font-size:13px;line-height:1.45;margin-bottom:20px;align-items:flex-start}
.contact-row svg{width:18px;height:18px;flex:none;margin-top:1px}
.field{width:236px;height:38px;background:#fff;color:#777;font-size:12px;padding:8px 12px;margin-bottom:8px}
.field.tall{height:72px}
.submit{display:inline-block;background:var(--green);color:#fff;font-size:14px;font-weight:600;padding:8px 18px}
.foot-mark{position:absolute;left:865px;top:72px;width:230px;text-align:center}
.foot-mark .dot{width:110px;height:110px;border-radius:50%;background:#fff;margin:0 auto}
.foot-mark .name{font-size:20px;font-weight:600;color:#fff;margin-top:16px}
.copyright{position:absolute;left:0;top:3783px;width:1200px;height:47px;background:var(--green);color:#fff;font-size:13px;font-weight:600;text-align:center;line-height:47px}
</style>
</head>
<body>

<header class="site-header">
  <div class="brand"><span class="brand-dot"></span><span class="brand-name">Kindred Ascent Partners</span></div>
  <a class="account login" href="#"><svg viewBox="0 0 16 16"><path d="M6 3h7v10H6M2 8h8M7 5l3 3-3 3" fill="none" stroke="#fff" stroke-width="1.8"/></svg>Login</a>
  <a class="account register" href="#"><svg viewBox="0 0 16 16"><circle cx="8" cy="5" r="3.2" fill="#fff"/><path d="M2 15c0-4 3-6 6-6s6 2 6 6z" fill="#fff"/></svg>Register</a>
</header>

<nav class="main-nav">
  <a class="active" href="#">Home</a><a href="#">About Us</a><a href="#">Coaching</a><a href="#">Services</a><a href="#">Shop</a><a href="#">Blog</a><a href="#">Testimonials</a><a href="#">Contact Us</a>
</nav>

<section class="hero" role="img" aria-label="Two climbers on a rocky summit, one reaching down to help the other, against a sunset sky">
  <h1>We Offer Life Coaching Business<br>To Individuals And Teams</h1>
  <a class="btn" href="#">Learn More</a>
</section>

<section class="about">
  <div class="about-photo" role="img" aria-label="Group yoga class holding tree pose on mats"></div>
  <h2>About <span>Kindred Ascent Partners</span></h2>
  <div class="divider"><i></i></div>
  <p>Lorem ipsum dolor sit amet, consectetuer adipiscing elit, sed diam nonummy nibh euismod tincidunt ut laoreet dolore magna aliquam erat volutpat. Ut wisi enim ad minim veniam, quis nostrud exerci tation ullamcorper suscipit lobortis nisl ut aliquip ex ea commodo consequat. Duis autem vel eum iriure dolor in hendrerit in vulputate velit esse molestie consequat, vel illum dolore eu feugiat nulla facilisis at vero eros et accumsan et iusto odio dignissim qui blandit praesent luptatum zzril</p>
  <a class="btn" href="#">Read More</a>
</section>

<section class="help">
  <h2 class="section-title">How We <span>Help You</span></h2>
  <div class="divider"><i></i></div>
  <p class="lead">Sed ut perspiciatis unde omnis iste natus error sit voluptatem accusantium doloremque laudantium, totam rem aperiam, eaque ipsa quae ab illo inventore veritatis et quasi architecto beatae vitae dicta sunt explicabo. Nemo enim ipsam voluptatem quia voluptas sit aspernatur aut odit aut fugit</p>
  <svg class="chev" style="left:56px" viewBox="0 0 24 40"><path d="M18 4 6 20l12 16" fill="none" stroke="#999" stroke-width="2"/></svg>
  <svg class="chev" style="left:1120px" viewBox="0 0 24 40"><path d="M6 4l12 16L6 36" fill="none" stroke="#999" stroke-width="2"/></svg>
  <div class="pillars">
    <div class="pillar">
      <svg viewBox="0 0 128 128"><circle cx="64" cy="66" r="52" fill="#fff"/><path d="M20 80a46 46 0 0 0 88 0" fill="none" stroke="#7dc142" stroke-width="6"/><g fill="#444"><rect x="34" y="52" width="8" height="26" rx="2"/><rect x="86" y="52" width="8" height="26" rx="2"/><rect x="42" y="58" width="6" height="14"/><rect x="80" y="58" width="6" height="14"/><rect x="48" y="62" width="32" height="6"/></g></svg>
      <h3>Physical</h3><p>Ut enim ad minim veniam, quis nostrud exercitation ullamco laboris nisi ut aliquip ex ea <b>[+]</b></p>
    </div>
    <div class="pillar">
      <svg viewBox="0 0 128 128"><circle cx="64" cy="66" r="52" fill="#fff"/><path d="M20 80a46 46 0 0 0 88 0" fill="none" stroke="#7dc142" stroke-width="6"/><circle cx="64" cy="64" r="28" fill="#444"/><circle cx="64" cy="64" r="10" fill="none" stroke="#fff" stroke-width="4"/><path d="M64 44v6M64 78v6M44 64h6M78 64h6" stroke="#fff" stroke-width="4" stroke-linecap="round"/></svg>
      <h3>Spiritual</h3><p>Ut enim ad minim veniam, quis nostrud exercitation ullamco laboris nisi ut aliquip ex ea <b>[+]</b></p>
    </div>
    <div class="pillar">
      <svg viewBox="0 0 128 128"><circle cx="64" cy="66" r="52" fill="#fff"/><path d="M20 80a46 46 0 0 0 88 0" fill="none" stroke="#7dc142" stroke-width="6"/><circle cx="64" cy="64" r="28" fill="none" stroke="#444" stroke-width="5"/><text x="64" y="76" text-anchor="middle" font-family="Open Sans,Arial,sans-serif" font-size="34" font-weight="700" fill="#444">$</text></svg>
      <h3>Financial</h3><p>Ut enim ad minim veniam, quis nostrud exercitation ullamco laboris nisi ut aliquip ex ea <b>[+]</b></p>
    </div>
    <div class="pillar">
      <svg viewBox="0 0 128 128"><circle cx="64" cy="66" r="52" fill="#fff"/><path d="M20 80a46 46 0 0 0 88 0" fill="none" stroke="#7dc142" stroke-width="6"/><g fill="#444"><rect x="40" y="66" width="12" height="16"/><rect x="58" y="52" width="12" height="30"/><rect x="76" y="42" width="12" height="40"/></g></svg>
      <h3>Leadership</h3><p>Ut enim ad minim veniam, quis nostrud exercitation ullamco laboris nisi ut aliquip ex ea <b>[+]</b></p>
    </div>
  </div>
</section>

<section class="services">
  <h2 class="section-title">Our <span class="cyan">Services</span></h2>
  <div class="divider"><i></i></div>
  <p class="lead">Sed ut perspiciatis unde omnis iste natus error sit voluptatem accusantium doloremque laudantium, totam rem aperiam, eaque ipsa quae ab illo inventore veritatis et quasi architecto beatae vitae dicta sunt explicabo. Nemo enim ipsam voluptatem quia voluptas sit aspernatur aut odit aut fugit, sed quia consequuntur magni dolores eos qui ratione voluptatem sequi nesciunt. Neque porro quisquam</p>
  <div class="services-mark"><div class="dot"></div><div class="name">Kindred Ascent Partners</div></div>
  <div class="services-rule"></div>
  <div class="service" style="top:268px"><h3>Professionals ( Career Coaching )</h3><p>Lorem ipsum dolor sit amet, consectetuer adipiscing elit, sed diam nonummy nibh euismod tincidunt ut laoreet dolore magna aliquam erat volutpat.</p></div>
  <div class="service" style="top:363px"><h3>Individuals ( Life Coaching )</h3><p>Lorem ipsum dolor sit amet, consectetuer adipiscing elit, sed diam nonummy nibh euismod tincidunt ut laoreet dolore magna aliquam erat volutpat. Consectetuer adipiscing elit.</p></div>
  <div class="service" style="top:457px"><h3>Executives ( Leadership Coaching )</h3><p>Lorem ipsum dolor sit amet, consectetuer adipiscing elit, sed diam nonummy nibh euismod tincidunt ut laoreet dolore magna aliquam erat volutpat. Consectetuer adipiscing elit.</p></div>
  <div class="service" style="top:544px"><h3>Working Mothers ( Career, Life &amp; Work / Life Balance Coaching )</h3><p>Lorem ipsum dolor sit amet, consectetuer adipiscing elit, sed diam nonummy nibh euismod tincidunt ut laoreet dolore magna aliquam erat volutpat. Consectetuer adipiscing elit.</p></div>
</section>

<section class="packages">
  <div class="packages-photo" role="img" aria-label="Smiling woman working on a laptop, tinted green"></div>
  <div class="packages-panel">
    <svg viewBox="0 0 90 90"><path d="M20 8h38l14 14v60H20z" fill="none" stroke="#fff" stroke-width="4"/><path d="M58 8v14h14" fill="none" stroke="#fff" stroke-width="4"/><path d="M38 30l16 10-16 10z" fill="#fff"/><path d="M30 60h32M30 70h32" stroke="#fff" stroke-width="4"/></svg>
    <h2>Our Packages Today</h2>
    <p>( Word Documents, Videos And Audio )</p>
    <a class="btn" href="#">Shop Now</a>
  </div>
  <div class="video-photo" role="img" aria-label="Video still of two women in a coaching conversation across a table"></div>
</section>

<section class="books">
  <h2 class="section-title">Check Out Our <span class="cyan">Bestselling Books</span></h2>
  <div class="divider"><i></i></div>
  <svg class="chev" style="left:56px;top:240px" viewBox="0 0 24 40"><path d="M18 4 6 20l12 16" fill="none" stroke="#999" stroke-width="2"/></svg>
  <svg class="chev" style="left:1120px;top:240px" viewBox="0 0 24 40"><path d="M6 4l12 16L6 36" fill="none" stroke="#999" stroke-width="2"/></svg>
  <div class="book-cover" role="img" aria-label="Blue book cover"></div>
  <div class="book-info">
    <h3>Ut enim ad minim veniam, quis nostrud exercitation ullamco laboris nisi ut aliquip ex ea</h3>
    <p>Sed ut perspiciatis unde omnis iste natus error sit voluptatem accusantium doloremque laudantium, totam rem aperiam, eaque ipsa quae ab illo inventore veritatis et quasi architecto beatae vitae dicta sunt explicabo. Nemo enim ipsam voluptatem quia voluptas sit aspernatur aut odit aut fugit, sed quia consequuntur magni dolores eos qui ratione voluptatem sequi</p>
    <a class="btn" href="#">Shop Now</a>
  </div>
</section>

<section class="community">
  <article class="card blog">
    <h2 class="card-title">Latest <span>Blog</span></h2>
    <div class="divider"><i></i></div>
    <div class="post"><div class="post-date">02<br>Mar</div><div><h4>Lorem ipsum dolor sit amet,</h4><p>Fusce elementum, nulla vel pellentes consequat, ante nulla hendrerit arcu, ac tincidunt mauris leo.</p></div></div>
    <div class="post"><div class="post-date">02<br>Mar</div><div><h4>Lorem ipsum dolor sit amet,</h4><p>Fusce elementum, nulla vel pellentes consequat, ante nulla hendrerit arcu, ac tincidunt mauris leo.</p></div></div>
  </article>
  <article class="card voices">
    <h2 class="card-title">What <span>People say about us?</span></h2>
    <div class="divider"><i></i></div>
    <div class="quote"><div class="avatar" role="img" aria-label="Client portrait"></div><p>“ Mattis porttitor nulla, eget eleifend metus gravida id . Nune sollicitudin nune at tellus pretium a pulvinar purus. Mattis porttitor null, eget eleifend mentus gravida id. Nune sollicitudin nune at tellus pretium a pulvinar purus. Nune sollicitudin nune at tellus...”</p></div>
  </article>
</section>

<footer class="site-footer">
  <div class="foot-col" style="left:100px">
    <h4>Quick Links</h4>
    <ul class="links"><li>Home</li><li>About Us</li><li>Coaching</li><li>Services</li><li>Shop</li><li>Blog</li><li>Testimonials</li><li>Contact Us</li></ul>
  </div>
  <div class="foot-col" style="left:302px;width:270px">
    <h4>Contact Details</h4>
    <div class="contact-row"><svg viewBox="0 0 18 18"><path d="M9 1a6 6 0 0 0-6 6c0 5 6 10 6 10s6-5 6-10a6 6 0 0 0-6-6z" fill="#fff"/><circle cx="9" cy="7" r="2.2" fill="#1b1b1b"/></svg><span>Kindred Ascent Partners<br>8100, Lorem ipsum dolor sit amet,<br>consectetuer adipiscing elit</span></div>
    <div class="contact-row"><svg viewBox="0 0 18 18"><circle cx="9" cy="9" r="8.5" fill="#fff"/><path d="M6 4.5l2 2-1 1.5c.8 1.6 1.9 2.7 3.5 3.5l1.5-1 2 2-1.5 1.5C8.5 13.5 4.5 9.5 4.5 6z" fill="#1b1b1b"/></svg><span>(123) 456-7890</span></div>
    <div class="contact-row"><svg viewBox="0 0 18 18"><circle cx="9" cy="9" r="8.5" fill="#fff"/><path d="M6 4.5l2 2-1 1.5c.8 1.6 1.9 2.7 3.5 3.5l1.5-1 2 2-1.5 1.5C8.5 13.5 4.5 9.5 4.5 6z" fill="#1b1b1b"/></svg><span>(123) 456-7890</span></div>
    <div class="contact-row"><svg viewBox="0 0 18 18"><circle cx="9" cy="9" r="8.5" fill="#fff"/><path d="M4.5 6h9v6h-9zM4.5 6l4.5 3.5L13.5 6" fill="none" stroke="#1b1b1b" stroke-width="1.3"/></svg><span>info@kindredascentpartners.com</span></div>
  </div>
  <div class="foot-col" style="left:597px">
    <h4>Contact Us</h4>
    <div class="field">Name</div>
    <div class="field">Email</div>
    <div class="field tall">Message</div>
    <span class="submit">Submit →</span>
  </div>
  <div class="foot-mark"><div class="dot"></div><div class="name">Kindred Ascent Partners</div></div>
</footer>
<div class="copyright">Copyright © 2017 Kindred Ascent Partners | All Rights Reserved</div>

</body>
</html>
```